Welding company needs a business card

We are looking for a logo and business card.

Contact Information for Business Card

418 Bramblecrest Lane
York, PA 17402
410-555-0173
Kvmetalcraft@forgepostbox.net

```html
<!DOCTYPE html>
<html lang="en">
<head>
<meta charset="utf-8">
<title>Kvmetalcraft – Business Card</title>
<link href="https://fonts.googleapis.com/css2?family=Source+Sans+3:wght@400&display=swap" rel="stylesheet">
<style>
  :root {
    --page-bg: #ffffff;
    --card-bg: #ffffff;
    --brand-blue: #1b4f82;
    --accent-orange: #e8532a;
    --text-dark: #3a3a3a;
    --card-edge: #d9dde2;
  }
  html, body {
    margin: 0;
    padding: 0;
    width: 1200px;
    height: 960px;
    overflow: hidden;
    background: var(--page-bg);
    font-family: "Source Sans 3", "Source Sans Pro", sans-serif;
  }
  .business-card {
    position: absolute;
    left: 286px;
    top: 300px;
    width: 630px;
    height: 360px;
    background: var(--card-bg);
    outline: 1px solid var(--card-edge);
    overflow: hidden;
  }
  .side-band {
    position: absolute;
    left: 0;
    top: 0;
    width: 66px;
    height: 100%;
    background: var(--brand-blue);
  }
  .brand-name {
    position: absolute;
    right: 37px;
    top: 110px;
    margin: 0;
    font-size: 38px;
    font-weight: 400;
    line-height: 1;
    letter-spacing: -0.5px;
    color: var(--brand-blue);
  }
  .address {
    position: absolute;
    right: 37px;
    top: 222px;
    margin: 0;
    font-style: normal;
    font-size: 17px;
    line-height: 26px;
    text-align: right;
    color: var(--text-dark);
  }
  .contact-list {
    position: absolute;
    right: 37px;
    top: 289px;
    margin: 0;
    padding: 0;
    list-style: none;
    font-size: 17px;
    line-height: 26px;
    color: var(--text-dark);
  }
  .contact-item {
    display: flex;
    justify-content: flex-end;
    align-items: center;
  }
  .contact-icon {
    width: 17px;
    height: 17px;
    margin-left: 13px;
    fill: var(--accent-orange);
  }
</style>
</head>
<body>
  <section class="business-card">
    <div class="side-band"></div>

    <h1 class="brand-name">Kvmetalcraft</h1>

    <address class="address">
      418 Bramblecrest Lane<br>
      York, PA 17402
    </address>

    <ul class="contact-list">
      <li class="contact-item">
        <span>410-555-0173</span>
        <svg class="contact-icon" viewBox="0 0 24 24" aria-hidden="true">
          <path d="M6.6 10.8a15.1 15.1 0 0 0 6.6 6.6l2.2-2.2c.3-.3.7-.4 1-.2 1.1.4 2.3.6 3.6.6.6 0 1 .4 1 1V20c0 .6-.4 1-1 1A17 17 0 0 1 3 4c0-.6.4-1 1-1h3.5c.6 0 1 .4 1 1 0 1.3.2 2.5.6 3.6.1.3 0 .7-.2 1z"/>
        </svg>
      </li>
      <li class="contact-item">
        <span>Kvmetalcraft@forgepostbox.net</span>
        <svg class="contact-icon" viewBox="0 0 24 24" aria-hidden="true">
          <path d="M2 5h20v14H2z M3.5 6.5 12 13l8.5-6.5v-.1H3.5z" fill-rule="evenodd"/>
          <path d="M2 5l10 8 10-8v1.6l-10 8-10-8z M2 19l7-6 1.2 1L3.6 19.5z M22 19l-7-6-1.2 1 6.6 5.5z" fill="#ffffff"/>
        </svg>
      </li>
    </ul>
  </section>
</body>
</html>
```